DEIJ Annual Progress Report

We need a Word-based year-end progress report for The Calloway Partners, Inc. for their client Brookvale Care Network. The report should be easily editable because this report represents the first draft. We want the report to use The Calloway Partners, Inc.'s colors as the main color and incorporate the client's colors as ascents. Please provide two spots per page where photos can be inserted.
Updates

Please include an introduction and conclusion paragraph. I will add that text later.

I uploaded the introduction and conclusion to use with the report.

Give some designer a chance to response, or update their designs.

Target Market(s)

Healthcare Executives

Industry/Entity Type

Healthcare consulting

Font styles to use
Other font styles liked:
• Loto, and Raleway

Requirements
Must have
• Use of the TCP and BVCN logos, appropriate photos in case I go with stock photos
Nice to have
• Warm but professional feeling
Should not have
• Cartoons, silly or funny pictures

```html
<!DOCTYPE html>
<html lang="en">
<head>
<meta charset="utf-8">
<title>2023 Progress Report – The Calloway Partners, Inc.</title>
<link href="https://fonts.googleapis.com/css2?family=Montserrat:wght@500;700;800;900&family=Raleway:wght@400;500;600;700&display=swap" rel="stylesheet">
<style>
:root{
  --navy:#1f1b5c;
  --gold:#b07c1e;
  --gold-soft:#c99a3e;
  --sky:#e3eef4;
  --sky-deep:#cfe2ec;
  --paper:#ffffff;
  --ink:#2b2b3a;
  --muted:#6b6b7a;
  --stage:#d8d8d8;
}
*{box-sizing:border-box;margin:0;padding:0}
html,body{width:1200px;height:2929px;overflow:hidden;background:var(--stage)}
body{font-family:"Raleway",sans-serif;color:var(--ink);position:relative}
.sheet{position:absolute;left:110px;width:980px;height:660px;display:flex;box-shadow:0 18px 40px rgba(0,0,0,.18)}
.sheet.cover{top:36px}
.sheet.partnership{top:768px}
.sheet.progress{top:1500px}
.sheet.next-steps{top:2232px}
.page{position:relative;width:490px;height:660px;overflow:hidden;background:var(--paper)}
.page.left{box-shadow:inset -14px 0 18px -14px rgba(0,0,0,.18)}
.page.right{box-shadow:inset 14px 0 18px -14px rgba(0,0,0,.18)}
.shapes{position:absolute;inset:0;width:100%;height:100%}
.photo{position:absolute}
.folio{position:absolute;bottom:22px;font:500 10px "Raleway",sans-serif;color:var(--muted)}
.folio.r{right:34px}.folio.l{left:34px}

/* brand name */
.brand{display:flex;align-items:center;gap:8px;font:800 13px/1.05 "Montserrat",sans-serif;color:var(--navy);text-transform:uppercase}
.brand .dot{width:26px;height:26px;border-radius:50%;border:4px solid var(--navy);flex:none}

/* cover */
.back-cover{background:linear-gradient(180deg,var(--sky-deep) 0%,var(--sky) 45%,var(--paper) 70%)}
.back-cover .brand{position:absolute;left:46px;top:450px}
.back-cover .contact{position:absolute;left:46px;top:510px;font:600 15px/1.6 "Raleway",sans-serif;color:var(--ink)}
.front-cover{background:var(--sky)}
.front-cover .brand{position:absolute;left:250px;top:70px}
.front-cover .year{position:absolute;left:230px;top:118px;font:500 40px "Montserrat",sans-serif;color:var(--gold);letter-spacing:2px}
.front-cover .title{position:absolute;left:200px;top:168px;font:900 40px/1 "Montserrat",sans-serif;color:var(--navy);text-transform:uppercase}

/* section titles in circles */
.circle-title{position:absolute;font:800 30px "Montserrat",sans-serif;color:#fff;text-align:center}

/* partnership list */
.timeline{position:absolute;left:38px;top:60px;width:420px}
.milestone{position:relative;padding-left:86px;height:180px}
.milestone .icon{position:absolute;left:0;top:0;width:64px;height:64px}
.milestone h3{font:800 17px/1.2 "Montserrat",sans-serif;color:var(--ink);margin-bottom:8px}
.milestone ul{list-style:none}
.milestone li{position:relative;padding-left:16px;font:500 11.5px/1.45 "Raleway",sans-serif;color:var(--muted);margin-bottom:3px}
.milestone li::before{content:"";position:absolute;left:0;top:4px;width:7px;height:7px;border:1.5px solid var(--muted);border-radius:50%}
.timeline .rail{position:absolute;left:31px;top:64px;width:1.5px;height:296px;background:var(--gold)}

/* progress */
.focus{position:absolute;width:270px}
.focus h4{font:800 14px/1.2 "Montserrat",sans-serif;color:var(--navy);margin-bottom:6px}
.focus h4 span{color:var(--gold)}
.focus p{font:500 9.5px/1.45 "Raleway",sans-serif;color:var(--muted);margin-bottom:3px}
.focus.to-right{text-align:right}
.progress .page.left{background:#fbfbfb}
.progress .page.right{background:#fbfbfb}

/* next steps */
.band-title{position:absolute;left:0;top:44px;width:470px;text-align:center;color:#fff}
.band-title .big{font:900 36px/1 "Montserrat",sans-serif;letter-spacing:1px}
.band-title .small{font:800 16px "Montserrat",sans-serif;letter-spacing:3px;margin-top:6px}
.steps{position:absolute;left:34px;top:70px;width:422px;display:grid;grid-template-columns:1fr 1fr;grid-auto-rows:170px;column-gap:0}
.step{padding:10px 14px;border-bottom:1px solid #e2e2e8}
.step:nth-child(odd){border-right:1px solid #e2e2e8}
.step:nth-last-child(-n+2){border-bottom:none}
.step .head{display:flex;gap:10px;align-items:center;margin-bottom:8px}
.step svg{flex:none;width:34px;height:34px}
.step h5{font:800 11.5px/1.2 "Montserrat",sans-serif;color:var(--ink)}
.step p{font:500 9.5px/1.5 "Raleway",sans-serif;color:var(--muted)}
</style>
</head>
<body>

<!-- COVER -->
<section class="sheet cover">
  <div class="page left back-cover">
    <svg class="shapes" viewBox="0 0 490 660" aria-hidden="true">
      <circle cx="120" cy="560" r="250" fill="var(--navy)"/>
      <circle cx="92" cy="580" r="212" fill="#fff"/>
      <circle cx="120" cy="560" r="272" fill="none" stroke="var(--gold)" stroke-width="1.5"/>
    </svg>
    <div class="brand"><span class="dot"></span>The Calloway<br>Partners, Inc.</div>
    <div class="contact">555 014 2290<br>www.callowaypartners.example</div>
  </div>
  <div class="page right front-cover">
    <div class="photo" role="img" aria-label="Photo of four smiling colleagues standing together" style="left:0;top:300px;width:490px;height:360px;background:linear-gradient(180deg,#b9cfd9,#7c6a5c 60%,#4a3c3a)"></div>
    <svg class="shapes" viewBox="0 0 490 660" aria-hidden="true">
      <circle cx="330" cy="140" r="300" fill="none" stroke="var(--navy)" stroke-width="1.5"/>
      <circle cx="330" cy="160" r="255" fill="var(--gold)"/>
      <circle cx="355" cy="140" r="220" fill="#fff"/>
    </svg>
    <div class="brand"><span class="dot"></span>The Calloway<br>Partners, Inc.</div>
    <div class="year">2023</div>
    <div class="title">Progress<br>Report</div>
  </div>
</section>

<!-- PARTNERSHIP -->
<section class="sheet partnership">
  <div class="page left">
    <div class="photo" role="img" aria-label="Photo of a team huddled in a circle, seen from below" style="inset:0;background:linear-gradient(135deg,#c9d3dc,#8a7868 50%,#3f4c66)"></div>
    <svg class="shapes" viewBox="0 0 490 660" aria-hidden="true">
      <circle cx="270" cy="300" r="200" fill="none" stroke="#fff" stroke-width="1.5"/>
      <circle cx="260" cy="310" r="175" fill="var(--gold)" opacity=".92"/>
      <circle cx="285" cy="295" r="138" fill="var(--navy)"/>
    </svg>
    <div class="circle-title" style="left:150px;top:275px;width:270px">Partnership</div>
  </div>
  <div class="page right">
    <div class="timeline">
      <div class="rail"></div>
      <div class="milestone">
        <svg class="icon" viewBox="0 0 64 64" aria-hidden="true"><circle cx="32" cy="32" r="30" fill="#fff" stroke="var(--gold)" stroke-width="2"/><circle cx="32" cy="32" r="23" fill="none" stroke="#ddd"/><path d="M20 36l8-6 6 4 10-8M20 40h24" fill="none" stroke="var(--navy)" stroke-width="2" stroke-linecap="round"/></svg>
        <h3>The Partnership Overview</h3>
        <ul>
          <li>Partnership Initiation: February 2022</li>
          <li>Purpose: Implementing the Anti-Racism Road Map</li>
          <li>Backbone Support within the Collective Impact Model</li>
        </ul>
      </div>
      <div class="milestone">
        <svg class="icon" viewBox="0 0 64 64" aria-hidden="true"><circle cx="32" cy="32" r="30" fill="#fff" stroke="var(--gold)" stroke-width="2"/><circle cx="32" cy="32" r="23" fill="none" stroke="#ddd"/><rect x="20" y="22" width="24" height="16" rx="2" fill="none" stroke="var(--navy)" stroke-width="2"/><path d="M26 44h12M32 38v6" stroke="var(--navy)" stroke-width="2"/></svg>
        <h3>Project Key Assumptions</h3>
        <ul>
          <li>Collective Impact Model guides strategy implementation</li>
          <li>Emphasis on change management and theories of change</li>
          <li>Commitment from BVCN to prioritize and resource the initiative</li>
        </ul>
      </div>
      <div class="milestone">
        <svg class="icon" viewBox="0 0 64 64" aria-hidden="true"><circle cx="32" cy="32" r="30" fill="#fff" stroke="var(--gold)" stroke-width="2"/><circle cx="32" cy="32" r="23" fill="none" stroke="#ddd"/><circle cx="32" cy="27" r="5" fill="none" stroke="var(--navy)" stroke-width="2"/><path d="M22 44c2-6 18-6 20 0" fill="none" stroke="var(--navy)" stroke-width="2"/></svg>
        <h3>The Role of The Calloway Partners, Inc</h3>
        <ul>
          <li>Providing Backbone Support as per the Collective Impact Model</li>
          <li>Developing a sustainable strategic architecture</li>
          <li>Supporting the establishment of working teams and providing consultative support</li>
        </ul>
      </div>
    </div>
    <div class="folio r">02</div>
  </div>
</section>

<!-- PROGRESS -->
<section class="sheet progress">
  <div class="page left">
    <div class="focus to-right" style="left:60px;top:60px">
      <h4><span>Guiding Vision</span> and Strategy</h4>
      <p>Facilitated the development of four strategic goals derived from 9 strategies.</p>
      <p>Spearheaded KPI and strategy card presentations to track progress and set priorities.</p>
      <p>Played a pivotal role in shaping goals and defining measures of success.</p>
      <p>Picture: KPI presentations and strategy cards that illustrate guidance.</p>
    </div>
    <div class="focus to-right" style="left:50px;top:245px">
      <h4><span>Supporting</span> Aligned Activities</h4>
      <p>Coaches worked closely with strategy leads to define actions for strategic advancement.</p>
      <p>Developed a coaching template integrating a learning journey within the team model.</p>
      <p>Ensured alignment and synergy among teams toward collective goals.</p>
      <p>Picture: documentation of the learning journey's integration with the leadership model.</p>
    </div>
    <div class="focus to-right" style="left:40px;top:440px">
      <h4><span>Establishing Shared</span><br>Measurement Practices</h4>
      <p>Led the creation of four overarching goals aligning with 9 strategies.</p>
      <p>Initiated the development of success measures and their transformation into indicators.</p>
      <p>Took charge of establishing shared goals and the methodology for measuring success.</p>
      <p>Picture: goals and objectives documents that show shared data in use.</p>
    </div>
    <div class="folio l">03</div>
  </div>
  <div class="page right">
    <div class="focus" style="left:200px;top:70px">
      <h4><span>Building</span> Public Will</h4>
      <p>Planned and participated in the D&amp;I Summit, with our CEO as a key speaker.</p>
      <p>Actively participated in executive diversity leadership forums (EDLF) meetings.</p>
      <p>Participated in internal and external sessions to gain visible support.</p>
      <p>Picture: Event snapshots and recordings, feedback from attendees and media coverage.</p>
    </div>
    <div class="focus" style="left:200px;top:270px">
      <h4><span>Fostering Continuous Learning</span><br>and Development</h4>
      <p>Integrated coaching with the existing leadership model, enriching depth with a learning focus.</p>
      <p>Embedded wellness and resilience-building within strategic development.</p>
      <p>The Calloway Partners, Inc CEO was actively involved in providing continuous learning.</p>
      <p>Picture: Descriptions of the coaching model and case studies of how the learning was applied.</p>
    </div>
    <div class="focus" style="left:180px;top:470px">
      <h4><span>Mobilizing</span> Funding</h4>
      <p>While not directly involved in funding, we've laid the groundwork for future investment.</p>
      <p>Articulated clear goals, success measures and metrics to support funding efforts.</p>
      <p>Preparing to benchmark progress on the measures suggested to attract sustainable resources.</p>
    </div>
    <div class="folio r">04</div>
  </div>
  <svg class="shapes" viewBox="0 0 980 660" aria-hidden="true" style="pointer-events:none">
    <circle cx="490" cy="330" r="150" fill="none" stroke="#c6c6d4" stroke-width="1.5"/>
    <circle cx="475" cy="340" r="108" fill="var(--gold)"/>
    <circle cx="500" cy="325" r="82" fill="var(--navy)"/>
    <g fill="#fff" stroke="var(--gold)" stroke-width="2">
      <circle cx="415" cy="200" r="24"/><circle cx="565" cy="200" r="24"/>
      <circle cx="340" cy="330" r="24"/><circle cx="640" cy="330" r="24"/>
      <circle cx="415" cy="460" r="24"/><circle cx="565" cy="460" r="24"/>
    </g>
    <g fill="none" stroke="var(--navy)" stroke-width="1.8" stroke-linecap="round">
      <rect x="405" y="191" width="20" height="16" rx="2"/>
      <path d="M556 210v-12h6v12M566 210v-16h6v16"/>
      <path d="M331 336l6-6 5 4 8-8"/>
      <circle cx="640" cy="330" r="7"/><path d="M640 319v4M640 337v4M629 330h4M647 330h4"/>
      <path d="M406 468c3-8 15-8 18 0M415 450v8"/>
      <circle cx="565" cy="456" r="5"/><path d="M556 470c2-6 16-6 18 0"/>
    </g>
    <text x="490" y="340" text-anchor="middle" font-family="Montserrat" font-weight="800" font-size="26" fill="#fff">Progress</text>
  </svg>
</section>

<!-- NEXT STEPS -->
<section class="sheet next-steps">
  <div class="page left">
    <div class="photo" role="img" aria-label="Photo of a therapist guiding a patient balancing on an exercise ball" style="left:0;top:150px;width:490px;height:510px;background:linear-gradient(180deg,#eceae6,#c7c3bd 60%,#8c7f78)"></div>
    <svg class="shapes" viewBox="0 0 490 660" aria-hidden="true">
      <ellipse cx="250" cy="40" rx="300" ry="170" fill="none" stroke="var(--ink)" stroke-width="1.2"/>
      <ellipse cx="250" cy="35" rx="290" ry="165" fill="var(--gold)"/>
      <ellipse cx="250" cy="10" rx="200" ry="150" fill="var(--navy)"/>
    </svg>
    <div class="band-title"><div class="big">NEXT STEPS</div><div class="small">GOVERNANCE</div></div>
  </div>
  <div class="page right">
    <div class="steps">
      <div class="step">
        <div class="head"><svg viewBox="0 0 34 34" aria-hidden="true"><circle cx="14" cy="14" r="8" fill="none" stroke="var(--navy)" stroke-width="2"/><path d="M20 20l8 8" stroke="var(--navy)" stroke-width="2"/></svg><h5>Reflective Review of the Roadmap's Focus:</h5></div>
        <p>Assess the need to adjust mission, operational planning and activities based on recent developments and participant feedback.</p>
      </div>
      <div class="step">
        <div class="head"><svg viewBox="0 0 34 34" aria-hidden="true"><rect x="5" y="6" width="24" height="22" fill="none" stroke="var(--navy)" stroke-width="2"/><path d="M10 22l5-6 4 3 6-8" fill="none" stroke="var(--navy)" stroke-width="2"/></svg><h5>Broadening Anti-Racism Efforts:</h5></div>
        <p>Reducing not just racism but also related forms like homophobia and anti-Semitism in future studies.</p>
      </div>
      <div class="step">
        <div class="head"><svg viewBox="0 0 34 34" aria-hidden="true"><circle cx="17" cy="17" r="7" fill="none" stroke="var(--navy)" stroke-width="2"/><path d="M17 4v5M17 25v5M4 17h5M25 17h5" stroke="var(--navy)" stroke-width="2"/></svg><h5>Operational Alignment:</h5></div>
        <p>Continue to assess and adjust the roadmap's governance structures based on recent developments, ensuring they stay aligned with overarching goals and strategies of the roadmap.</p>
      </div>
      <div class="step">
        <div class="head"><svg viewBox="0 0 34 34" aria-hidden="true"><path d="M4 18l7-6 6 4 6-4 7 6-7 7-6-4-6 4z" fill="none" stroke="var(--navy)" stroke-width="2" stroke-linejoin="round"/></svg><h5>Commitment and Support Structures:</h5></div>
        <p>Reinforce the commitment from all of Brookvale Care Network to the anti-racism roadmap and ensure structures support active participation and contribution at various levels.</p>
      </div>
      <div class="step">
        <div class="head"><svg viewBox="0 0 34 34" aria-hidden="true"><circle cx="11" cy="12" r="4" fill="none" stroke="var(--navy)" stroke-width="2"/><circle cx="23" cy="12" r="4" fill="none" stroke="var(--navy)" stroke-width="2"/><path d="M4 27c1-6 13-6 14 0M16 27c1-6 13-6 14 0" fill="none" stroke="var(--navy)" stroke-width="2"/></svg><h5>Enhanced Operational Communication:</h5></div>
        <p>Implement robust internal communication strategies to inform all stakeholders about the roadmap's progress, challenges and next stages, fostering transparency and building trust among the team members.</p>
      </div>
      <div class="step">
        <div class="head"><svg viewBox="0 0 34 34" aria-hidden="true"><rect x="4" y="8" width="26" height="18" fill="none" stroke="var(--navy)" stroke-width="2"/><path d="M10 20h14M10 15h8" stroke="var(--navy)" stroke-width="2"/></svg><h5>Training and Development for Operational Staff</h5></div>
        <p>Provide targeted training and development programs for staff involved in the operational aspects of the roadmap. This ensures they have the skills and knowledge to effectively contribute to the initiative.</p>
      </div>
    </div>
    <div class="folio r">06</div>
  </div>
</section>

</body>
</html>
```